KVO-Business Card Design

I need a modern, professional business card design that includes my logo as the main feature, maybe the entire background with the contact info overlaying or even contact info on the back and the logo full frontal

Neat and organized placement of contact information

Would like to see options in black and white

Target Market(s)

real estate Developers, Construction managers, business and home owners

Industry/Entity Type

Construction

Contact Information for Business Card

KVO Construction
Danny Ferrante
General Contractor

Office: 1-888-902-7315 Ext #1
Cell: 215-730-4162
Fax: 1-888-902-7315

Font styles to use
Serif

Requirements
Must have
• title
• office #
• cell #
• Email
• website
Nice to have
• fax

```html
<!DOCTYPE html>
<html lang="en">
<head>
<meta charset="utf-8">
<title>KVO Construction Business Card</title>
<link href="https://fonts.googleapis.com/css2?family=Jost:wght@400;500;600&display=swap" rel="stylesheet">
<style>
  :root {
    --bg: #3f5a44;
    --card: #ffffff;
    --green: #0f8a3a;
    --green-dark: #0b6a2c;
    --green-light: #1fae4e;
    --stripe: #ededed;
    --ink: #1c1c1c;
    --rule: #111111;
  }
  * { box-sizing: border-box; margin: 0; padding: 0; }
  html, body { width: 1200px; height: 800px; overflow: hidden; }
  body {
    background: var(--bg);
    font-family: "Jost", sans-serif;
    position: relative;
  }
  .card {
    position: absolute;
    top: 246px;
    width: 540px;
    height: 308px;
    background: var(--card);
    overflow: hidden;
    box-shadow: 0 10px 30px rgba(0,0,0,.35);
  }
  /* Front */
  .card-front { left: 45px; }
  .front-brand {
    position: absolute;
    left: 0; right: 0; top: 104px;
    display: flex; align-items: center; justify-content: center; gap: 16px;
  }
  .brand-mark { width: 30px; height: 30px; background: var(--green); }
  .front-brand .brand-name {
    font-size: 46px; font-weight: 600; color: var(--green-dark);
    text-transform: uppercase; letter-spacing: .5px;
  }
  .front-rule {
    position: absolute; left: 0; right: 0; bottom: 26px;
    height: 5px; background: var(--green-dark);
  }
  .front-edge {
    position: absolute; left: 0; right: 0; bottom: 0;
    height: 16px; background: var(--green-dark);
  }
  /* Back */
  .card-back { left: 615px; }
  .holder-name {
    position: absolute; left: 28px; top: 26px;
    font-size: 31px; font-weight: 400; color: var(--green-dark);
  }
  .back-brand {
    position: absolute; right: 24px; top: 44px;
    display: flex; align-items: center; gap: 8px;
  }
  .back-brand .brand-mark { width: 14px; height: 14px; }
  .back-brand .brand-name {
    font-size: 19px; font-weight: 400; color: var(--green-dark);
  }
  .title-band {
    position: absolute; left: 0; right: 0; top: 94px; height: 40px;
    background: linear-gradient(90deg, var(--green-dark), var(--green-light) 55%, var(--green));
    border-top: 4px solid var(--rule);
    border-bottom: 2px solid var(--rule);
  }
  .title-band .job-title {
    position: absolute; left: 42px; top: 3px;
    font-size: 22px; color: #fff; font-weight: 400;
  }
  .contact-list {
    position: absolute; left: 0; right: 0; top: 134px;
    list-style: none;
  }
  .contact-list li {
    height: 24px; display: flex; align-items: center;
    padding-left: 26px; gap: 10px;
    font-size: 14px; color: var(--ink);
  }
  .contact-list li:nth-child(odd) { background: var(--stripe); }
  .contact-list svg { width: 13px; height: 13px; flex: none; }
  .back-edge {
    position: absolute; left: 0; right: 0; bottom: 0;
    height: 26px; background: linear-gradient(180deg, var(--stripe), #fff);
  }
</style>
</head>
<body>
  <section class="card card-front" aria-label="Business card front">
    <div class="front-brand">
      <span class="brand-mark"></span>
      <span class="brand-name">KVO Construction</span>
    </div>
    <div class="front-rule"></div>
    <div class="front-edge"></div>
  </section>

  <section class="card card-back" aria-label="Business card back">
    <h1 class="holder-name">Danny Ferrante</h1>
    <div class="back-brand">
      <span class="brand-mark"></span>
      <span class="brand-name">KVO Construction</span>
    </div>
    <div class="title-band"><span class="job-title">General Contractor</span></div>
    <ul class="contact-list">
      <li>
        <svg viewBox="0 0 16 16"><path d="M3 2h3l1 3-2 1.5a9 9 0 0 0 4.5 4.5L11 9l3 1v3a1 1 0 0 1-1 1A11 11 0 0 1 2 3a1 1 0 0 1 1-1z" fill="#1c1c1c"/></svg>
        1-888-902-7315 Ext #1
      </li>
      <li>
        <svg viewBox="0 0 16 16"><rect x="4" y="1" width="8" height="14" rx="1.5" fill="none" stroke="#1c1c1c" stroke-width="1.5"/><circle cx="8" cy="12.5" r=".9" fill="#1c1c1c"/></svg>
        215-730-4162
      </li>
      <li>
        <svg viewBox="0 0 16 16"><rect x="4" y="1" width="8" height="4" fill="#1c1c1c"/><rect x="1" y="5" width="14" height="6" rx="1" fill="#1c1c1c"/><rect x="4" y="10" width="8" height="5" fill="#fff" stroke="#1c1c1c"/></svg>
        1-888-902-7315
      </li>
      <li>
        <svg viewBox="0 0 16 16"><rect x="1" y="3" width="14" height="10" fill="#1c1c1c"/><path d="M1.5 3.5 8 9l6.5-5.5" fill="none" stroke="#fff" stroke-width="1.3"/></svg>
        danny@kvoconstruction.com
      </li>
      <li>
        <svg viewBox="0 0 16 16"><rect x="1.5" y="2" width="13" height="9" fill="none" stroke="#1c1c1c" stroke-width="1.5"/><path d="M6 14h4M8 11v3" stroke="#1c1c1c" stroke-width="1.5"/></svg>
        www.kvoconstruction.com
      </li>
    </ul>
    <div class="back-edge"></div>
  </section>
</body>
</html>
```